The Vigor Depot needs a postcard design.

We need a postcard design for our new retail/consignment store called "The Vigor Depot". We buy, sell and consign gently used exercise equipment. We offer treadmills, ellipticals, gyms, bikes and more. We can save our customers up to 50% off retail prices. We also offer delivery, set-up, removal/recycling of old equipment, and repair. Our initial product/business (and formerly store name) is RoadWell Gym Service - our mobile business that offers repairs & service/maintenance. We would like this postcard to focus only on The Vigor Depot and be bright, colorful and cheerful, inviting the community to come in and see how we can fit them with the right piece of equipment both physically and economically.
We specialize in buying, selling and consigning pre-owned equipment.

The overall design should be informative about who we are, what we offer, and one that communicates we are inviting them to stop by and check us out.

Thank you!!

Target Market(s)

People wanting to work out at home on a budget.
The elderly, rehab patients, moms wanting pre-baby body back,
health conscience people as well as appeal the the younger crowd.

Industry/Entity Type

Fitness Equipment

Font styles to use
Serif

Colors
3276b5
33a6d7
0393ce
33b8a4
add136
fbee3d
ffcf3e
faa54b

Requirements
Must have
• our logo, address: 4870 Birch Ln. SE Salem, Or 97306, phone #: 971-555-0187
• lots of color-
• Caption of " Save up to 50% off of retail prices
• "We deliver" "Delivery Available"
Nice to have
• We like the design idea of layering images, transparent images in the background and the use of lots of color that engages the potential customer.
• Website or QR code - www.thevigordepot-example.net
Should not have
• Realistic images of people or exercise equipment. Should not be tailored after our RoadWell website. This is a completely different business. We want to stay away from the red/black color scheme. Also should not mention "NEW". We do not want the focus to be on new equipment.

```html
<!DOCTYPE html>
<html lang="en">
<head>
<meta charset="utf-8">
<title>The Vigor Depot – Postcard</title>
<link rel="stylesheet" href="https://fonts.googleapis.com/css2?family=Oswald:wght@400;500;600;700&family=Open+Sans:wght@400;600;700&display=swap">
<style>
  :root {
    --page-bg: #e6e8eb;
    --blue-deep: #3276b5;
    --blue-bright: #0393ce;
    --blue-sky: #33a6d7;
    --teal: #33b8a4;
    --lime: #add136;
    --yellow: #fbee3d;
    --gold: #ffcf3e;
    --orange: #faa54b;
    --headline-yellow: #f9c531;
    --ink: #3a3a3a;
    --grey-text: #555b62;
    --white: #ffffff;
  }
  * { box-sizing: border-box; margin: 0; padding: 0; }
  html, body {
    width: 806px; height: 1200px; overflow: hidden;
    background: var(--page-bg);
    font-family: "Open Sans", Arial, sans-serif;
  }
  .postcard {
    position: absolute; overflow: hidden; background: var(--white);
    box-shadow: 0 2px 8px rgba(0,0,0,.18);
  }
  .postcard-front { left: 78px; top: 60px; width: 655px; height: 508px; }
  .postcard-back  { left: 78px; top: 617px; width: 658px; height: 510px; }
  .card-shapes { position: absolute; inset: 0; }

  .brand-name {
    position: absolute; left: 40px; top: 38px;
    display: flex; align-items: center; gap: 12px;
    font-family: "Oswald", sans-serif; font-weight: 600; font-size: 34px;
    color: var(--blue-deep); letter-spacing: .5px;
  }
  .brand-dot { width: 22px; height: 22px; border-radius: 50%; background: var(--orange); }

  .offer { position: absolute; left: 18px; top: 156px; width: 310px; text-align: center; font-family: "Oswald", sans-serif; }
  .offer-lead { font-size: 38px; font-weight: 700; color: var(--blue-deep); line-height: 1; }
  .offer-sub { font-size: 17px; font-weight: 600; color: var(--blue-deep); margin-top: 6px; letter-spacing: .3px; line-height: 1.1; }
  .offer-big { font-size: 46px; font-weight: 700; color: var(--blue-deep); line-height: 1; margin-top: 2px; }
  .offer-tail { font-family: "Open Sans", sans-serif; font-size: 23px; font-weight: 400; color: var(--grey-text); margin-top: 4px; letter-spacing: .5px; }

  .perk {
    position: absolute; top: 312px; width: 80px; height: 80px;
    display: flex; flex-direction: column; justify-content: center; align-items: center;
    text-align: center; font-family: "Oswald", sans-serif; font-weight: 600; line-height: 1.05;
  }
  .perk-main { font-size: 14px; color: var(--blue-deep); }
  .perk-accent { font-size: 14px; color: var(--lime); }
  .perk-note { font-size: 6px; color: var(--lime); font-family: "Open Sans", sans-serif; }
  .perk-cash { left: 35px; }
  .perk-warranty { left: 135px; }
  .perk-consign { left: 235px; }

  .contact { position: absolute; left: 20px; top: 414px; color: var(--grey-text); }
  .contact-address { display: flex; align-items: center; gap: 6px; font-size: 15px; }
  .contact-hours { font-size: 15px; font-weight: 600; color: var(--blue-bright); margin-left: 22px; }
  .contact-row { display: flex; align-items: center; gap: 8px; margin-top: 6px; }
  .contact-phone { font-family: "Oswald", sans-serif; font-size: 20px; font-weight: 600; color: var(--blue-bright); }
  .contact-web { font-size: 12px; font-weight: 700; color: var(--blue-bright); }

  .deals { position: absolute; right: 16px; top: 40px; text-align: center; }
  .deals-main { font-family: "Oswald", sans-serif; font-size: 44px; font-weight: 700; color: var(--headline-yellow); line-height: 1; }
  .deals-sub { font-size: 26px; font-weight: 600; color: var(--white); line-height: 1.3; letter-spacing: .3px; }

  .about-title {
    position: absolute; left: 16px; top: 32px;
    font-family: "Oswald", sans-serif; font-size: 26px; font-weight: 600; color: var(--blue-deep);
  }
  .about-text {
    position: absolute; left: 16px; top: 77px; width: 296px;
    font-size: 14px; line-height: 1.22; color: var(--ink); font-weight: 600;
  }
  .back-phone {
    position: absolute; left: 28px; top: 382px; display: flex; align-items: center; gap: 8px;
    font-family: "Oswald", sans-serif; font-size: 30px; font-weight: 600; color: var(--blue-deep);
  }
  .back-web {
    position: absolute; left: 32px; top: 422px; display: flex; align-items: center; gap: 12px;
    font-size: 11px; font-weight: 700; color: var(--ink);
  }
</style>
</head>
<body>

<section class="postcard postcard-front">
  <svg class="card-shapes" width="655" height="508" viewBox="0 0 655 508">
    <defs>
      <linearGradient id="front-orange" x1="0" y1="0" x2="0" y2="1">
        <stop offset="0" stop-color="#ffb03b"/>
        <stop offset="1" stop-color="#ffcf3e"/>
      </linearGradient>
      <linearGradient id="front-photo" x1="0" y1="0" x2="0" y2="1">
        <stop offset="0" stop-color="#8c8e92"/>
        <stop offset=".45" stop-color="#d7d9dc"/>
        <stop offset="1" stop-color="#4e3a31"/>
      </linearGradient>
    </defs>
    <rect width="655" height="508" fill="#f4f5f6"/>
    <rect x="0" y="126" width="420" height="9" fill="var(--blue-sky)"/>
    <rect x="0" y="138" width="420" height="240" fill="url(#front-orange)"/>
    <rect x="0" y="345" width="420" height="12" fill="var(--blue-bright)"/>
    <rect x="0" y="380" width="420" height="128" fill="#f4f5f6"/>
    <circle cx="75" cy="352" r="42" fill="var(--white)" stroke="var(--blue-bright)" stroke-width="4"/>
    <circle cx="175" cy="352" r="42" fill="var(--white)" stroke="var(--blue-bright)" stroke-width="4"/>
    <circle cx="275" cy="352" r="42" fill="var(--white)" stroke="var(--blue-bright)" stroke-width="4"/>
    <path d="M404 0 Q 285 250 436 508" fill="none" stroke="var(--blue-sky)" stroke-width="16"/>
    <path d="M412 0 Q 320 250 446 508" fill="none" stroke="var(--white)" stroke-width="5"/>
    <g role="img" aria-label="Photo of a gym floor with weight machines and benches">
      <path d="M420 0 Q 310 250 452 508 L655 508 L655 0 Z" fill="url(#front-photo)"/>
    </g>
    <path d="M420 0 Q 310 250 452 508" fill="none" stroke="var(--blue-deep)" stroke-width="5"/>
  </svg>

  <div class="brand-name"><span class="brand-dot"></span>The Vigor Depot</div>

  <div class="offer">
    <p class="offer-lead">STOP IN &amp; SEE US</p>
    <p class="offer-sub">WE CAN SAVE OUR CUSTOMERS</p>
    <p class="offer-big">UP TO 50% OFF</p>
    <p class="offer-tail">RETAIL PRICES</p>
  </div>

  <div class="perk perk-cash"><span class="perk-main">CASH FOR</span><span class="perk-accent">YOURS</span></div>
  <div class="perk perk-warranty"><span class="perk-main">30 DAYS<br>WARRANTY</span><span class="perk-note">ASK FOR DETAILS</span></div>
  <div class="perk perk-consign"><span class="perk-main">CONSIGN</span><span class="perk-accent">E-MADE<br>E-Z</span></div>

  <div class="contact">
    <p class="contact-address">
      <svg width="16" height="14" viewBox="0 0 16 14"><path d="M1 7 L8 1 L15 7 M3 6 V13 H13 V6" fill="none" stroke="var(--blue-bright)" stroke-width="1.6"/></svg>
      4870 Birch Ln. SE Salem, Or 97306
    </p>
    <p class="contact-hours">Tues-Sat 10:30-5pm</p>
    <p class="contact-row">
      <svg width="16" height="16" viewBox="0 0 16 16"><rect width="16" height="16" rx="3" fill="var(--lime)"/><path d="M5 3 L7 6 L6 7 Q7 9 9 10 L10 9 L13 11 L12 13 Q6 13 3 5 Z" fill="var(--white)"/></svg>
      <span class="contact-phone">971-555-0187</span>
      <svg width="12" height="12" viewBox="0 0 12 12"><circle cx="6" cy="6" r="5" fill="none" stroke="var(--lime)" stroke-width="1.3"/><path d="M1 6 H11 M6 1 V11" stroke="var(--lime)" stroke-width="1"/></svg>
      <span class="contact-web">www.thevigordepot-example.net</span>
    </p>
  </div>

  <div class="deals">
    <p class="deals-main">GOOD DEALS</p>
    <p class="deals-sub">FINALLY HERE</p>
  </div>
</section>

<section class="postcard postcard-back">
  <svg class="card-shapes" width="658" height="510" viewBox="0 0 658 510">
    <defs>
      <linearGradient id="back-orange" x1="0" y1="0" x2="1" y2="1">
        <stop offset="0" stop-color="#ffa92f"/>
        <stop offset="1" stop-color="#ffd23e"/>
      </linearGradient>
    </defs>
    <rect width="658" height="510" fill="var(--white)"/>
    <path d="M0 0 L290 0 Q 425 255 268 510 L0 510 Z" fill="url(#back-orange)"/>
    <path d="M298 0 Q 436 255 276 510" fill="none" stroke="var(--blue-deep)" stroke-width="8"/>
    <path d="M310 0 Q 452 255 290 510" fill="none" stroke="var(--blue-sky)" stroke-width="4"/>
    <rect x="124" y="50" width="60" height="3" fill="var(--teal)"/>
    <rect x="124" y="58" width="72" height="3" fill="var(--teal)"/>
    <rect x="0" y="205" width="362" height="140" fill="var(--blue-bright)"/>
    <g role="img" aria-label="Photo of a cable weight machine">
      <rect x="0" y="220" width="96" height="108" fill="#c9cdd1"/>
    </g>
    <g role="img" aria-label="Photo of a rack of dumbbells">
      <rect x="107" y="220" width="130" height="108" fill="#4d4f52"/>
    </g>
    <g role="img" aria-label="Photo of a warehouse full of exercise equipment">
      <rect x="244" y="220" width="114" height="108" fill="#8f8a80"/>
    </g>
    <rect x="556" y="43" width="83" height="82" fill="none" stroke="#222" stroke-width="1.5"/>
    <line x1="410" y1="158" x2="642" y2="158" stroke="#b8b8b8"/>
    <line x1="410" y1="193" x2="642" y2="193" stroke="#b8b8b8"/>
    <line x1="410" y1="229" x2="642" y2="229" stroke="#b8b8b8"/>
  </svg>

  <h2 class="about-title">About Us</h2>
  <p class="about-text">We buy, sell and consign gently used exercise equipment.We offer treadmills, ellipticals, gyms, bikes and more. We also offer delivery, set-up, removal/recycling of old equipment, and repair.</p>

  <p class="back-phone">
    <svg width="24" height="24" viewBox="0 0 16 16"><rect width="16" height="16" rx="3" fill="var(--blue-bright)"/><path d="M5 3 L7 6 L6 7 Q7 9 9 10 L10 9 L13 11 L12 13 Q6 13 3 5 Z" fill="var(--white)"/></svg>
    971-555-0187
  </p>
  <p class="back-web">
    <svg width="14" height="14" viewBox="0 0 12 12"><circle cx="6" cy="6" r="5" fill="none" stroke="var(--blue-bright)" stroke-width="1.3"/><path d="M1 6 H11 M6 1 V11" stroke="var(--blue-bright)" stroke-width="1"/></svg>
    www.thevigordepot-example.net
  </p>
</section>

</body>
</html>
```